Accommodation business card design

We need a business card designed for our long-term accommodation business based in Australia. The business card must match the style of the attached letterhead and logo. The same contact details that are on the letterhead will also go on the card except that the card must list the contact details in the following order:phone, email, home address, ABN.

The card will be printed on .76mm white pvc plastic (same as credit cards), printed both sides and will be silver foil stamped on at least one side (preferably 2 sides) The design template is attached, but please go to www.qz-cardworks.com.au for more specs.

The only other addition the card will be my name: Dalwyn Prothero

Industry/Entity Type

Accommodation

```html
<!DOCTYPE html>
<html lang="en">
<head>
<meta charset="utf-8">
<title>Ridgeline Accommodation – Business Card</title>
<link rel="stylesheet" href="https://fonts.googleapis.com/css2?family=Open+Sans:wght@400;800&family=Reenie+Beanie&display=swap">
<style>
  :root {
    --maroon: #6B1D3B;
    --brown: #8A4B40;
    --paper: #FFFFFF;
    --edge: #8C8C8C;
    --script: #C9A3B4;
    --ink-light: #FFFFFF;
  }
  * { box-sizing: border-box; margin: 0; padding: 0; }
  html, body {
    width: 1200px; height: 998px; overflow: hidden;
    background: var(--paper);
    font-family: "Open Sans", Arial, sans-serif;
  }
  .stage { position: relative; width: 1200px; height: 998px; }
  .card {
    position: absolute; top: 334px;
    width: 492px; height: 309px;
    border-radius: 22px; overflow: hidden;
  }
  .card--front { left: 53px; background: var(--paper); border: 1px solid var(--edge); }
  .card--back { left: 659px; background: var(--maroon); }

  .front-band {
    position: absolute; left: 0; right: 0; bottom: 0; height: 92px;
    background: linear-gradient(90deg, var(--brown) 0%, var(--brown) 45%, var(--maroon) 100%);
  }

  .brand { position: absolute; left: 82px; top: 77px; display: flex; align-items: center; gap: 16px; }
  .brand__square { width: 96px; height: 101px; border-radius: 12px; background: var(--maroon); }
  .brand__name {
    color: var(--brown); font-weight: 800; line-height: 1;
    text-transform: uppercase;
  }
  .brand__name-main { display: block; font-size: 40px; letter-spacing: 0.5px; }
  .brand__name-sub { display: block; font-size: 21px; margin-top: 6px; letter-spacing: 0.2px; }

  .holder {
    position: absolute; left: 54px; top: 36px;
    font-family: "Reenie Beanie", cursive;
    font-size: 44px; color: var(--script); line-height: 1;
  }
  .rule { position: absolute; left: 54px; right: 0; top: 98px; height: 2px; background: var(--ink-light); }

  .contacts { list-style: none; color: var(--ink-light); font-size: 18px; }
  .contacts li {
    position: absolute; left: 52px;
    display: flex; align-items: center; height: 26px;
    white-space: nowrap;
  }
  .contacts .row-phone { top: 118px; }
  .contacts .row-email { top: 152px; }
  .contacts .row-post { top: 181px; }
  .contacts .row-abn { top: 215px; }
  .contacts .icon { width: 22px; height: 22px; margin-right: 10px; flex: none; }
  .contacts .no-icon { margin-left: 32px; }
</style>
</head>
<body>
<main class="stage">
  <section class="card card--front" aria-label="Card front">
    <div class="front-band" role="img" aria-label="Decorative brown and maroon wave band along the lower edge"></div>
    <div class="brand">
      <div class="brand__square"></div>
      <div class="brand__name">
        <span class="brand__name-main">Ridgeline</span>
        <span class="brand__name-sub">Accommodation</span>
      </div>
    </div>
  </section>

  <section class="card card--back" aria-label="Card back">
    <p class="holder">Dalwyn Prothero</p>
    <div class="rule"></div>
    <ul class="contacts">
      <li class="row-phone">
        <svg class="icon" viewBox="0 0 22 22" aria-hidden="true">
          <circle cx="11" cy="11" r="11" fill="var(--ink-light)"/>
          <path d="M8 5.5 L10 8.5 L8.8 10 C9.5 11.8 10.5 12.9 12 13.4 L13.5 12.2 L16.5 14.2 L15 16.5 C10 16.5 5.5 12 5.5 7 Z" fill="var(--maroon)"/>
        </svg>
        <span>0400 555 218</span>
      </li>
      <li class="row-email">
        <svg class="icon" viewBox="0 0 22 22" aria-hidden="true">
          <circle cx="11" cy="11" r="11" fill="var(--ink-light)"/>
          <rect x="5" y="7" width="12" height="8.5" fill="var(--maroon)"/>
          <path d="M5 7 L11 12 L17 7" fill="none" stroke="var(--ink-light)" stroke-width="1.2"/>
        </svg>
        <span>dalwyn.prothero@example.com</span>
      </li>
      <li class="row-post">
        <svg class="icon" viewBox="0 0 22 22" aria-hidden="true">
          <circle cx="11" cy="11" r="11" fill="var(--ink-light)"/>
          <path d="M4.5 11 L11 5 L17.5 11 L16 11 L16 17 L6 17 L6 11 Z" fill="var(--maroon)"/>
          <rect x="9.6" y="12.5" width="2.8" height="4.5" fill="var(--ink-light)"/>
        </svg>
        <span>PO Box 1820, Bayside Mail Centre QLD 4700</span>
      </li>
      <li class="row-abn"><span class="no-icon">ABN 51 824 367 209</span></li>
    </ul>
  </section>
</main>
</body>
</html>
```